Business Card Design for Kidlarko (Hires out childrens play areas)

Looking to have a business card designed for a company we just bought. The company rents out childrens play areas.

I have uploaded a couple of examples of the kind of business card style I like. Here are two more examples:

https://vesterlingstudio.example.nz/project/brisk-romp-branding/
https://imgvaultcdn.example.com/design_img/8462913/307481/307481_2958174_8462913_a7c3e190_image.jpg

I think a white card will be best due to all the colours in the logo.

Size we require: 3.75" x 2.25" (horizontally orientated) with a 0.125" bleed

Uploaded is two versions of our logo.

Details for the card:
1. My name: Wade Ferrin
2. Title: Managing Director
3. Phone no: 021 537 462
4. Email: wade@kidlarko.example.nz
5. URL: www.kidlarko.example.nz
6. Address:
PO Box 381627
Fernmoor, Auckland

Let me know if you need anything else.

Target Market(s)

Hospitals, doctors surgeries, bed shops, etc.

Contact Information for Business Card

Details for the card:
1. My name: Wade Ferrin
3. Phone no: 021 537 462
5. URL: www.kidlarko.example.nz
6. Address:
PO Box 381627
Fernmoor, Auckland

Requirements
Should not have
• Not too busy.

```html
<!DOCTYPE html>
<html lang="en">
<head>
<meta charset="utf-8">
<title>Kidlarko Business Card</title>
<link href="https://fonts.googleapis.com/css2?family=Lato:wght@400;700&display=swap" rel="stylesheet">
<style>
  :root {
    --backdrop: #1c1c1e;
    --purple: #7a3189;
    --green: #3bb54a;
    --white: #ffffff;
    --ink-purple: #7a3189;
  }
  * { margin: 0; padding: 0; box-sizing: border-box; }
  html, body {
    width: 1200px; height: 912px; overflow: hidden;
    background: var(--backdrop);
    font-family: "Lato", sans-serif;
  }
  .canvas { position: relative; width: 1200px; height: 912px; }

  .card {
    position: absolute;
    width: 560px; height: 336px;
    overflow: hidden;
    box-shadow: 0 14px 30px rgba(0,0,0,0.55);
  }

  /* Front */
  .card-front { left: 60px; top: 70px; background: var(--purple); }
  .front-brand {
    position: absolute; left: 0; right: 0; top: 118px;
    display: flex; justify-content: center; align-items: center; gap: 14px;
  }
  .brand-dot {
    width: 26px; height: 26px; border-radius: 50%;
    background: var(--green);
  }
  .front-brand .brand-name {
    color: var(--white); font-weight: 700; font-size: 50px; letter-spacing: 1px;
  }
  .front-url {
    position: absolute; left: 0; right: 0; top: 262px;
    text-align: center; color: var(--white); font-size: 15px; letter-spacing: 0.5px;
  }

  /* Back */
  .card-back { left: 580px; top: 486px; background: var(--white); }
  .back-bands { position: absolute; inset: 0; width: 560px; height: 336px; }
  .back-brand {
    position: absolute; left: 40px; top: 72px;
    display: flex; align-items: center; gap: 12px;
  }
  .back-brand .brand-name {
    color: var(--ink-purple); font-weight: 700; font-size: 46px; letter-spacing: 1px;
  }
  .holder {
    position: absolute; right: 26px; top: 162px; text-align: right; color: var(--white);
  }
  .holder-name { font-weight: 700; font-size: 20px; line-height: 1.1; }
  .holder-title { font-size: 13px; margin-top: 2px; }
  .address {
    position: absolute; right: 26px; top: 226px; text-align: right;
    color: var(--white); font-size: 15px; line-height: 1.35;
  }
  .contacts {
    position: absolute; left: 26px; top: 272px;
    list-style: none; color: var(--white); font-size: 15px;
  }
  .contacts li { display: flex; align-items: center; gap: 10px; line-height: 1.35; }
  .contacts svg { width: 13px; height: 13px; fill: var(--white); flex: none; }
</style>
</head>
<body>
<div class="canvas">

  <section class="card card-front">
    <div class="front-brand">
      <span class="brand-dot"></span>
      <span class="brand-name">Kidlarko</span>
    </div>
    <p class="front-url">www.kidlarko.example.nz</p>
  </section>

  <section class="card card-back">
    <svg class="back-bands" viewBox="0 0 560 336" preserveAspectRatio="none" aria-hidden="true">
      <path d="M0 242 L560 112 L560 336 L0 336 Z" fill="var(--green)"/>
      <path d="M0 258 L220 208 C245 203 255 216 285 214 L560 200 L560 336 L0 336 Z" fill="var(--purple)"/>
    </svg>

    <div class="back-brand">
      <span class="brand-dot"></span>
      <span class="brand-name">Kidlarko</span>
    </div>

    <div class="holder">
      <p class="holder-name">Wade Ferrin</p>
      <p class="holder-title">Managing Director</p>
    </div>

    <p class="address">PO Box 381627<br>Fernmoor, Auckland</p>

    <ul class="contacts">
      <li>
        <svg viewBox="0 0 24 24"><path d="M6.6 10.8a15.1 15.1 0 0 0 6.6 6.6l2.2-2.2a1 1 0 0 1 1-.25 11.4 11.4 0 0 0 3.6.57 1 1 0 0 1 1 1V20a1 1 0 0 1-1 1A17 17 0 0 1 3 4a1 1 0 0 1 1-1h3.5a1 1 0 0 1 1 1c0 1.25.2 2.45.57 3.57a1 1 0 0 1-.25 1z"/></svg>
        021 537 462
      </li>
      <li>
        <svg viewBox="0 0 24 24"><path d="M2 5h20v14H2z M2 5l10 8 10-8" fill="none" stroke="#fff" stroke-width="2"/></svg>
        wade@kidlarko.example.nz
      </li>
      <li>
        <svg viewBox="0 0 24 24"><circle cx="12" cy="12" r="10" fill="none" stroke="#fff" stroke-width="2"/><path d="M2 12h20M12 2c3 3 3 17 0 20M12 2c-3 3-3 17 0 20" fill="none" stroke="#fff" stroke-width="1.6"/></svg>
        www.kidlarko.example.nz
      </li>
    </ul>
  </section>

</div>
</body>
</html>
```